Quorvin 2025 Landing Page Image for www.quorvin-example.com

Hello please find the old landing page for a new startup called Quorvin. (www.quorvin-example.com) The company is in the sports area. We have a new logo for 2025 that is attached. We need a new landing page that says "Coming 2H 2025" Looking for something slightly different and exciting. Please find the new logo and old image attached.

Target Market(s)

Sports Media

Industry/Entity Type

Sports Media

Requirements
Must have
• Text: "Quorvin 2.0 Coming 2H 2025"

```html
<!DOCTYPE html>
<html lang="en">
<head>
<meta charset="utf-8">
<title>Quorvin 2.0 – Coming 2H 2025</title>
<link rel="stylesheet" href="https://fonts.googleapis.com/css2?family=Roboto:wght@400;500;700&display=swap">
<style>
  :root {
    --bg: #0b0b0b;
    --text: #ffffff;
    --muted: #c4c4c4;
    --nav: #cfcfcf;
    --lime: #9bd61e;
    --orange: #ec7a4c;
    --card: rgba(30, 30, 30, 0.85);
    --card-border: rgba(255, 255, 255, 0.12);
    --input: #2a2a2a;
  }
  * { box-sizing: border-box; margin: 0; padding: 0; }
  html, body { width: 1200px; height: 977px; overflow: hidden; }
  body {
    position: relative;
    background: var(--bg);
    color: var(--text);
    font-family: "Roboto", sans-serif;
  }
  .backdrop {
    position: absolute; inset: 0;
    background:
      radial-gradient(circle at 726px 782px, #232323 0, #181818 120px, rgba(12,12,12,0) 200px),
      radial-gradient(ellipse at 900px 120px, #1c1c1c 0, rgba(13,13,13,0) 55%),
      linear-gradient(180deg, #050505 0%, #111111 55%, #0a0a0a 100%);
  }
  .header-brand {
    position: absolute; left: 64px; top: 46px;
    font-size: 23px; font-weight: 500; color: var(--lime); line-height: 26px;
  }
  .nav { position: absolute; top: 49px; left: 0; font-size: 18px; line-height: 22px; color: var(--nav); }
  .nav a { position: absolute; color: inherit; text-decoration: none; white-space: nowrap; }
  .hero-brand {
    position: absolute; left: 0; width: 1200px; top: 228px;
    text-align: center; font-size: 62px; line-height: 72px; font-weight: 700; color: var(--lime);
  }
  .version {
    position: absolute; left: 713px; top: 224px; width: 48px; height: 28px;
    border-radius: 14px; border: 1.5px solid var(--lime);
    border-right-color: var(--orange); border-bottom-color: var(--orange);
    font-size: 17px; font-weight: 500; line-height: 25px; text-align: center;
  }
  .headline {
    position: absolute; left: 0; width: 1198px; top: 348px; text-align: center;
    font-size: 20px; line-height: 26px; font-weight: 700;
  }
  .tagline {
    position: absolute; left: 0; width: 1205px; top: 380px; text-align: center;
    font-size: 17px; line-height: 22px; font-weight: 500; color: var(--lime);
  }
  .countdown { position: absolute; left: 418px; top: 427px; display: flex; gap: 19px; }
  .unit { width: 76px; text-align: center; }
  .unit-box {
    height: 77px; border-radius: 7px; background: linear-gradient(180deg, #2a2a2a, #1c1c1c);
    border: 1px solid rgba(255,255,255,0.14); border-top-color: rgba(155,214,30,0.35);
    font-size: 38px; font-weight: 700; line-height: 75px;
  }
  .unit-label { margin-top: 8px; font-size: 11px; font-weight: 500; color: var(--muted); }
  .features { position: absolute; left: 246px; top: 578px; display: flex; gap: 21px; }
  .feature {
    width: 222px; height: 116px; border-radius: 8px; background: var(--card);
    border: 1px solid var(--card-border); text-align: center; padding: 22px 20px 0;
  }
  .feature h2 { font-size: 17px; line-height: 22px; font-weight: 700; margin-bottom: 7px; }
  .feature p { font-size: 11px; line-height: 15px; color: var(--muted); }
  .notify-title {
    position: absolute; left: 0; width: 1190px; top: 756px; text-align: center;
    font-size: 17px; line-height: 22px; font-weight: 700;
  }
  .notify-form { position: absolute; left: 421px; top: 789px; display: flex; gap: 8px; }
  .email-field {
    width: 234px; height: 39px; border-radius: 4px; background: var(--input);
    border: 1px solid rgba(255,255,255,0.12); color: var(--muted);
    font: 400 11px "Roboto", sans-serif; padding: 0 13px; line-height: 37px;
  }
  .notify-btn {
    width: 114px; height: 39px; border-radius: 3px; border: none;
    background: linear-gradient(90deg, var(--lime) 35%, var(--orange));
    font: 500 11px "Roboto", sans-serif; color: #111;
    display: flex; align-items: center; justify-content: center; gap: 12px;
  }
  .footer-note {
    position: absolute; left: 40px; top: 919px; font-size: 12px; line-height: 16px; color: var(--muted);
  }
  .social { position: absolute; left: 1083px; top: 921px; display: flex; gap: 14px; }
  .social span { width: 12px; height: 12px; border-radius: 50%; border: 1.5px solid var(--muted); }
</style>
</head>
<body>
  <div class="backdrop" role="img" aria-label="Dark photo of a football resting on grass at night"></div>

  <div class="header-brand">Quorvin</div>
  <nav class="nav">
    <a style="left:855px" href="#">Features</a>
    <a style="left:962px" href="#">Roadmap</a>
    <a style="left:1075px" href="#">FAQ</a>
  </nav>

  <h1 class="hero-brand">Quorvin</h1>
  <div class="version">2.0</div>

  <p class="headline">Coming 2H 2025</p>
  <p class="tagline">Bigger, Better, Bolder!</p>

  <div class="countdown">
    <div class="unit"><div class="unit-box">00</div><div class="unit-label">Days</div></div>
    <div class="unit"><div class="unit-box">00</div><div class="unit-label">Hours</div></div>
    <div class="unit"><div class="unit-box">00</div><div class="unit-label">Minutes</div></div>
    <div class="unit"><div class="unit-box">00</div><div class="unit-label">Seconds</div></div>
  </div>

  <section class="features">
    <article class="feature">
      <h2>Advanced Analytics</h2>
      <p>Deeper insights into player and team performance with AI-powered analytics.</p>
    </article>
    <article class="feature">
      <h2>Global Coverage</h2>
      <p>Expanded coverage of leagues and tournaments from around the world.</p>
    </article>
    <article class="feature">
      <h2>Real-Time Updates</h2>
      <p>Lightning-fast updates and notifications for all your favourite teams.</p>
    </article>
  </section>

  <h3 class="notify-title">Get notified when we launch</h3>
  <div class="notify-form">
    <div class="email-field">Enter your email</div>
    <button class="notify-btn">Notify Me
      <svg width="14" height="12" viewBox="0 0 14 12" fill="none" stroke="#111" stroke-width="1.6" stroke-linecap="round" stroke-linejoin="round"><path d="M1 6h12M8 1l5 5-5 5"/></svg>
    </button>
  </div>

  <footer>
    <p class="footer-note">2025 Quorvin Sports Analytics. All rights reserved.</p>
    <div class="social"><span></span><span></span><span></span></div>
  </footer>
</body>
</html>
```